Sturdyflow Mechanical - Letterhead

We are a plumbing and hvac company based in Calgary. This letterhead will be on our quotes, invoices, preventative maintenance proposals etc.

```html
<!DOCTYPE html>
<html lang="en">
<head>
<meta charset="utf-8">
<title>Sturdyflow Mechanical – Letterhead</title>
<link rel="stylesheet" href="https://fonts.googleapis.com/css2?family=Encode+Sans+Condensed:wght@300;700&family=Lato:wght@400&display=swap">
<style>
  :root {
    --brand-blue: #1f72b8;
    --brand-orange: #ef5a28;
    --ink: #555555;
    --ink-soft: #666666;
    --paper: #ffffff;
    --backdrop: #dcdcdc;
  }
  * { box-sizing: border-box; margin: 0; padding: 0; }
  html, body { width: 1056px; height: 1200px; overflow: hidden; }
  body { background: var(--backdrop); position: relative; }

  .letterhead {
    position: absolute; left: 128px; top: 35px;
    width: 800px; height: 1130px;
    background: var(--paper);
    overflow: hidden;
  }

  .brand {
    position: absolute; left: 0; right: 0; top: 58px;
    display: flex; flex-direction: column; align-items: center; gap: 16px;
  }
  .brand-dot {
    width: 92px; height: 92px; border-radius: 50%;
    background: var(--brand-orange);
  }
  .brand-name {
    font-family: "Encode Sans Condensed", sans-serif;
    font-weight: 700; font-size: 38px; letter-spacing: 1px;
    text-transform: uppercase; color: var(--brand-blue); line-height: 1;
  }

  .letter-body {
    position: absolute; left: 74px; width: 649px; top: 321px;
    font-family: "Encode Sans Condensed", sans-serif;
    font-weight: 300; font-size: 17.5px; line-height: 28px;
    color: var(--ink);
  }
  .letter-body p { text-align: justify; margin-bottom: 28px; }
  .letter-body .salutation { margin-bottom: 24px; }

  .sign-off {
    position: absolute; left: 74px; top: 890px;
    font-family: "Encode Sans Condensed", sans-serif;
    font-weight: 300; font-size: 17.5px; color: var(--ink);
  }
  .signature {
    position: absolute; left: 71px; top: 924px;
    width: 64px; height: 42px;
    background: linear-gradient(90deg, rgba(239,90,40,0.35), rgba(239,90,40,0.15));
    border-radius: 4px;
  }

  .contact-bar {
    position: absolute; left: 80px; top: 1052px;
    display: flex; align-items: center;
    font-family: "Lato", sans-serif; font-size: 13px; line-height: 15px;
    color: var(--ink-soft);
  }
  .contact-group { display: flex; flex-direction: column; gap: 1px; }
  .contact-line { display: flex; align-items: center; gap: 7px; }
  .contact-line svg { width: 10px; height: 10px; flex: none; }
  .divider { width: 1px; height: 24px; background: var(--brand-orange); margin: 0 40px; }
  .contact-phone .divider-after { }
  .address { padding-left: 0; }

  .footer-band { position: absolute; left: 0; bottom: 0; width: 800px; height: 19px; display: block; }
</style>
</head>
<body>
  <main class="letterhead">
    <header class="brand">
      <span class="brand-dot"></span>
      <span class="brand-name">Sturdyflow Mechanical</span>
    </header>

    <section class="letter-body">
      <p class="salutation">Dear Sir/Mam,</p>
      <p>Contrary to popular belief, Lorem Ipsum is not simply random text. It has roots in a piece of classical Latin literature from 45 BC, making it over 2000 years old. Daniel Hartwell, a Latin professor at Westbrook College in Alberta, looked up one of the more obscure Latin words, consectetur.</p>
      <p>Lorem Ipsum comes from sections 1.10.32 and 1.10.33 of "de Finibus Bonorum et Malorum" (The Extremes of Good and Evil) by Cicero, written in 45 BC. This book is a treatise on the theory of ethics, very popular during the Renaissance. The first line of Lorem Ipsum.</p>
      <p>The standard chunk of Lorem Ipsum used since the 1500s is reproduced below for those interested. Sections 1.10.32 and 1.10.33 from "de Finibus Bonorum et Malorum" by Cicero are also reproduced in their exact original.</p>
      <p>The standard chunk of Lorem Ipsum used since the 1500s is reproduced below for those interested.</p>
    </section>

    <p class="sign-off">Best Regards</p>
    <div class="signature" role="img" aria-label="Handwritten signature of Hartley"></div>

    <footer class="contact-bar">
      <div class="contact-group">
        <span class="contact-line">
          <svg viewBox="0 0 10 10"><path fill="#ef5a28" d="M2 0.5l1.8 2-1 1.1c.6 1.3 1.4 2.1 2.6 2.6l1.1-1 2 1.8-1.2 1.8C4.4 8.6 1.4 5.6.6 1.8z"/></svg>
          403-555-0142
        </span>
        <span class="contact-line">
          <svg viewBox="0 0 10 10"><rect x="2.5" y="0.5" width="5" height="3" fill="#ef5a28"/><rect x="0.5" y="3.5" width="9" height="4" rx="1" fill="#ef5a28"/><rect x="2.5" y="6.5" width="5" height="3" fill="#ef5a28"/></svg>
          403-555-0187
        </span>
      </div>
      <span class="divider"></span>
      <div class="contact-group">
        <span class="contact-line">
          <svg viewBox="0 0 10 10"><rect x="0.5" y="2" width="9" height="6.5" fill="#ef5a28"/><path d="M0.8 2.3L5 5.6l4.2-3.3" stroke="#fff" stroke-width="0.9" fill="none"/></svg>
          hello@sturdyflow.ca
        </span>
        <span class="contact-line">
          <svg viewBox="0 0 10 10"><circle cx="5" cy="5" r="4.3" fill="none" stroke="#ef5a28" stroke-width="0.9"/><ellipse cx="5" cy="5" rx="1.8" ry="4.3" fill="none" stroke="#ef5a28" stroke-width="0.8"/><path d="M0.7 5h8.6" stroke="#ef5a28" stroke-width="0.8"/></svg>
          www.sturdyflow.ca
        </span>
      </div>
      <span class="divider"></span>
      <div class="contact-group address">
        <span>1450 Ogden Road SE</span>
        <span>Calgary, AB T2C 1B4</span>
      </div>
    </footer>

    <svg class="footer-band" viewBox="0 0 800 19" preserveAspectRatio="none" aria-hidden="true">
      <polygon points="0,0 580,0 561,19 0,19" fill="#1f72b8"/>
      <polygon points="590,0 800,0 800,19 571,19" fill="#ef5a28"/>
    </svg>
  </main>
</body>
</html>
```